Website for my photography business

I need a website for my photography business, Jonah Pelling Photography. I need a website that has a landing page with a cover photo of each kind of photography I do. For example, Nature, Weddings, Portraits and Architecture. I want it so that when someone comes onto my website they have to choose which kind of photography page they want to visit. So if they click on the wedding photo it will open to a page with my wedding portfolio images and a contact me button. If they choose nature photography I want them to be redirected to an e-commerce section where they can purchase prints. Architecture and Portraits should open up to their respective portfolios with about me and contact info. I like this kind of format because I want people who come to my website for a specific type of photography to be able to be directed there easily without having to look at a mix of other kinds of photography. I will provide a few files to use as placeholders. I have already purchased the jonahpellingphotography.example domain name. A Wix website would be great because I am most familiar with it but I am open to anything.

Industry/Entity Type

Photographer

Number of Pages Required

5+ page

Requirements
Must have
• Landing Page and e-commerce

```html
<!DOCTYPE html>
<html lang="en">
<head>
<meta charset="utf-8">
<title>Jonah Pelling Photography</title>
<link rel="stylesheet" href="https://fonts.googleapis.com/css2?family=Poppins:wght@300;400;500&family=Prata&family=Courgette&display=swap">
<style>
:root{
  --accent:#fbb03b;
  --accent-soft:#fde7c2;
  --navy:#11122a;
  --ink:#26285c;
  --body:#6b6b78;
  --line:#ececf0;
  --white:#ffffff;
  --ghost:#eff2f4;
}
*{margin:0;padding:0;box-sizing:border-box}
html,body{width:1200px;height:3458px;overflow:hidden}
body{position:relative;font-family:'Poppins',sans-serif;background:var(--white);color:var(--body)}
h1,h2{font-weight:400}
.abs{position:absolute}
/* hero */
.hero{left:0;top:0;width:1200px;height:677px;background:linear-gradient(180deg,#2b3238 0%,#3d464b 35%,#2a2c2a 70%,#1b1a18 100%)}
.hero-photo{left:0;top:0;width:1200px;height:677px;background:radial-gradient(ellipse 300px 380px at 600px 330px,rgba(150,160,165,.45),rgba(0,0,0,0) 70%)}
.logo{left:77px;top:44px;color:var(--white);font-size:20px;font-weight:300;letter-spacing:.3px}
.nav-link{position:absolute;top:50px;color:var(--white);font-size:16px;text-decoration:none;white-space:nowrap}
.cart{left:1080px;top:38px;width:41px;height:41px;border-radius:50%;background:var(--accent)}
.hero-title{left:0;top:258px;width:1200px;text-align:center;font-family:'Prata',serif;color:var(--white);font-size:47px;line-height:58px;font-weight:400}
.btn{display:block;background:var(--accent);color:var(--white);font-size:20px;text-align:center;text-decoration:none;text-transform:uppercase}
.hero-btn{position:absolute;left:506px;top:393px;width:186px;height:57px;line-height:57px}
.mouse{left:589px;top:598px}
/* grid */
.gridline{width:1px;background:var(--line)}
/* about */
.ghost{left:70px;top:918px;font-size:200px;font-weight:500;color:var(--ghost);letter-spacing:-2px;line-height:1}
.pattern{background:var(--accent-soft)}
.portrait{left:401px;top:778px;width:396px;height:489px;background:radial-gradient(ellipse 140px 190px at 230px 170px,#4a4a4e,#1c1c20 75%)}
.hi{left:0;top:1322px;width:1200px;text-align:center;font-family:'Courgette',cursive;color:var(--ink);font-size:22px}
.name{left:0;top:1358px;width:1200px;text-align:center;color:var(--ink);font-size:49px;font-weight:400}
.hl{position:relative;display:inline-block;z-index:0}
.hl::after{content:"";position:absolute;left:0;right:0;bottom:8px;height:10px;background:var(--accent);z-index:-1}
.bio{left:340px;top:1432px;width:520px;text-align:center;font-size:14.5px;line-height:27px}
.bio p{margin-bottom:17px}
.more{left:0;top:1610px;width:1200px;text-align:center;font-size:16px}
.more a{color:var(--ink)}
/* photography */
.work{left:0;top:1727px;width:1200px;height:626px;background:var(--navy)}
.work-title{left:77px;top:1794px;color:var(--white);font-size:46px;font-weight:400}
.work-sub{left:131px;top:1874px;color:var(--white);font-size:15.5px;line-height:30px}
.tile{top:1978px;width:300px;height:286px}
.tile span{position:absolute;left:0;bottom:26px;width:100%;text-align:center;color:var(--white);font-size:24px}
/* adventure */
.adv-photo{left:227px;top:2502px;width:365px;height:353px;background:linear-gradient(180deg,#c7c8cc 0%,#b9b5b0 35%,#8a6a52 55%,#4f5a30 80%,#3a4424 100%)}
.adv-title{left:705px;top:2555px;font-family:'Courgette',cursive;color:var(--ink);font-size:45px;line-height:48px;font-weight:400}
.adv-sub{left:708px;top:2668px;font-size:17px;color:var(--body)}
.arrow{top:2712px;width:53px;height:53px;border:1px solid var(--accent)}
/* footer */
.footer{left:0;top:2967px;width:1200px;height:491px;background:var(--navy)}
.magic{left:131px;top:3014px;font-family:'Courgette',cursive;color:var(--white);font-size:43px;font-weight:400}
.magic-sub{left:133px;top:3074px;color:var(--white);font-size:16px}
.footer-btn{position:absolute;left:887px;top:3037px;width:187px;height:57px;line-height:57px}
.thumb{top:3155px;width:146px;height:146px}
.flinks{left:122px;top:3348px;color:var(--white);font-size:15px}
.flinks span{margin:0 9px}
.copy{left:122px;top:3376px;color:var(--white);font-size:15px}
.social{top:3350px;width:46px;height:46px;border:1.5px solid var(--accent);border-radius:50%}
.social svg{display:block}
</style>
</head>
<body>

<section class="abs hero">
  <div class="abs hero-photo" role="img" aria-label="Misty forest path with a hiker walking away between tall trees"></div>
  <div class="abs logo">Jonah Pelling Photography</div>
  <nav>
    <a class="nav-link" href="#" style="left:690px">Home</a>
    <a class="nav-link" href="#" style="left:765px">About Me</a>
    <a class="nav-link" href="#" style="left:868px">Photography</a>
    <a class="nav-link" href="#" style="left:997px">Contact</a>
  </nav>
  <div class="abs cart">
    <svg width="41" height="41" viewBox="0 0 41 41"><path d="M12 14h3l3 10h9l2-7H16" fill="none" stroke="#fff" stroke-width="1.6" stroke-linejoin="round"/><circle cx="19" cy="27.5" r="1.5" fill="#fff"/><circle cx="26" cy="27.5" r="1.5" fill="#fff"/></svg>
  </div>
  <h1 class="abs hero-title">Hi. I am a Photographer.<br>I Capture Life moments</h1>
  <a class="btn hero-btn" href="#">Contact Us</a>
  <svg class="abs mouse" width="24" height="40" viewBox="0 0 24 40"><rect x="1.5" y="1.5" width="21" height="37" rx="10.5" fill="none" stroke="#fff" stroke-width="2"/><line x1="12" y1="8" x2="12" y2="14" stroke="#fff" stroke-width="2"/></svg>
</section>

<div class="abs gridline" style="left:208px;top:677px;height:1050px"></div>
<div class="abs gridline" style="left:416px;top:677px;height:1050px"></div>
<div class="abs gridline" style="left:625px;top:677px;height:1050px"></div>
<div class="abs gridline" style="left:835px;top:677px;height:1050px"></div>
<div class="abs gridline" style="left:1044px;top:677px;height:1050px"></div>
<div class="abs gridline" style="left:208px;top:2353px;height:614px"></div>
<div class="abs gridline" style="left:416px;top:2353px;height:614px"></div>
<div class="abs gridline" style="left:625px;top:2353px;height:614px"></div>
<div class="abs gridline" style="left:835px;top:2353px;height:614px"></div>
<div class="abs gridline" style="left:1044px;top:2353px;height:614px"></div>

<section class="about">
  <div class="abs ghost">About Me</div>
  <div class="abs pattern" style="left:305px;top:841px;width:99px;height:181px" role="img" aria-label="Decorative accent pattern"></div>
  <div class="abs pattern" style="left:799px;top:1057px;width:101px;height:180px" role="img" aria-label="Decorative accent pattern"></div>
  <div class="abs portrait" role="img" aria-label="Black and white portrait of the photographer"></div>
  <svg class="abs" style="left:723px;top:1114px" width="116" height="114"><polygon points="116,0 116,114 0,114" fill="#fbb03b"/></svg>
  <div class="abs hi">Hi I'm</div>
  <h2 class="abs name"><span class="hl">Jonah</span> Pelling</h2>
  <div class="abs bio">
    <p>Lorem Ipsum is simply dummy text of the printing and typesetting industry Lorem Ipsum has been the</p>
    <p>Lorem Ipsum is simply dummy text of the printing and typesetting industry. Lorem Ipsum has been the industry's standard dummy text ever since the 1500s, when an unknown printer took a galley.</p>
  </div>
  <div class="abs more"><a href="#">Learn More</a></div>
</section>

<section class="abs work"></section>
<h2 class="abs work-title"><span class="hl">Photo</span>graphy</h2>
<div class="abs work-sub">Hi. I am a Photographer. I Capture Lifemoments<br>Lorem Ipsum is simply dummy.</div>
<div class="abs tile" style="left:0;background:linear-gradient(160deg,#3c4a3e,#8a7a68 55%,#d9dbe0)" role="img" aria-label="Red fox standing in snowy woods"><span>Nature</span></div>
<div class="abs tile" style="left:300px;background:linear-gradient(160deg,#6f6d62,#8c887c 50%,#5c5a52)" role="img" aria-label="Wedding ring resting on a stone"><span>Wedding</span></div>
<div class="abs tile" style="left:600px;background:linear-gradient(160deg,#2e2e2e,#6d6d6d 50%,#3a3a3a)" role="img" aria-label="Black and white portrait study"><span>Portraits</span></div>
<div class="abs tile" style="left:900px;background:linear-gradient(180deg,#c9cbcc,#8b6a58 45%,#5f5a55)" role="img" aria-label="Modern brick campus building"><span>Architecture</span></div>

<section class="adventure">
  <div class="abs pattern" style="left:152px;top:2447px;width:220px;height:44px" role="img" aria-label="Decorative accent pattern"></div>
  <div class="abs pattern" style="left:152px;top:2491px;width:75px;height:136px" role="img" aria-label="Decorative accent pattern"></div>
  <div class="abs adv-photo" role="img" aria-label="Stone castle tower on a grassy hillside"></div>
  <svg class="abs" style="left:495px;top:2769px" width="116" height="115"><polygon points="116,0 116,115 0,115" fill="#fbb03b"/></svg>
  <h2 class="abs adv-title">latest<br>Advanture</h2>
  <div class="abs adv-sub">Nature Photography</div>
  <div class="abs arrow" style="left:707px;background:var(--accent)">
    <svg width="51" height="51"><polyline points="29,17 21,25.5 29,34" fill="none" stroke="#fff" stroke-width="1.8"/></svg>
  </div>
  <div class="abs arrow" style="left:769px">
    <svg width="51" height="51"><polyline points="22,17 30,25.5 22,34" fill="none" stroke="#fbb03b" stroke-width="1.8"/></svg>
  </div>
</section>

<footer class="abs footer"></footer>
<h2 class="abs magic">let's Create Some Magic</h2>
<div class="abs magic-sub">Jonah Pelling Photography</div>
<a class="btn footer-btn" href="#">Contact Us</a>
<div class="abs thumb" style="left:125px;background:linear-gradient(160deg,#d8d8d8,#6a6a6a)" role="img" aria-label="Wedding couple portrait"></div>
<div class="abs thumb" style="left:286px;background:linear-gradient(160deg,#7a4a3a,#b07a60)" role="img" aria-label="Close portrait with leaves"></div>
<div class="abs thumb" style="left:447px;background:linear-gradient(180deg,#cfd1d3,#8d6e5c 55%,#6a6a6a)" role="img" aria-label="Brick building exterior"></div>
<div class="abs thumb" style="left:608px;background:linear-gradient(160deg,#e4e0dc,#a8222a 60%,#d8c8bc)" role="img" aria-label="Hands holding a ring on red petals"></div>
<div class="abs thumb" style="left:769px;background:linear-gradient(160deg,#3a3a3a,#9a9a9a)" role="img" aria-label="Black and white portrait"></div>
<div class="abs thumb" style="left:930px;background:linear-gradient(160deg,#f2eeec,#d8a8b8 55%,#ece6e2)" role="img" aria-label="Wedding rings with pink ribbon"></div>
<div class="abs flinks">Home<span>|</span>About Me<span>|</span>Photography<span>|</span>Contact</div>
<div class="abs copy">©Jonah Pelling - 2020 All rights reserved.</div>
<a class="abs social" href="#" style="left:971px" aria-label="Follow">
  <svg width="43" height="43" viewBox="0 0 43 43"><path d="M21.5 29.5l-7-6.8a4.2 4.2 0 0 1 7-4.6 4.2 4.2 0 0 1 7 4.6z" fill="none" stroke="#fbb03b" stroke-width="1.8" stroke-linejoin="round"/></svg>
</a>
<a class="abs social" href="#" style="left:1025px" aria-label="Share">
  <svg width="43" height="43" viewBox="0 0 43 43"><circle cx="15" cy="21.5" r="2.6" fill="none" stroke="#fbb03b" stroke-width="1.8"/><circle cx="27.5" cy="14.5" r="2.6" fill="none" stroke="#fbb03b" stroke-width="1.8"/><circle cx="27.5" cy="28.5" r="2.6" fill="none" stroke="#fbb03b" stroke-width="1.8"/><path d="M17.3 20.2l7.9-4.4M17.3 22.8l7.9 4.4" stroke="#fbb03b" stroke-width="1.8"/></svg>
</a>

</body>
</html>
```